Two Day Training Event includes a Dinner/Bowling Party at Larkspur in Troy, MI

I would like a postcard to attract Insurance Agents to an QWT meeting calling it a summit or something like that. Just something to mail to insurance agents telling them about our upcoming event with over 20 carriers. An opportunity to certify face to face with MAPD carriers and see what 2020 has to offer. Prior to OEP OPen Enrollment and AEP Annual Election period we have a number of meetings. Carriers want to come especially if we can get a number of agents. We are going to go to Larkspur a fun bowling alley for dinner, drinks and bowling to network and talk about the upcoming year.

Target Market(s)

Existing and new insurance agents

Industry/Entity Type

Insurance Broker

Contact Information for Business Card

Looking for a new card design I sent my LOGO and can upload my existing card.

Font styles to use
Serif

Colors

Designer to choose colors to be used in the design.

Requirements
Must have
• Dates Sept 16 and 17th
• location Harrowgate Conference Hall in Troy MI
• times
Nice to have
• It would be nice to see a fun design.

```html
<!DOCTYPE html>
<html lang="en">
<head>
<meta charset="utf-8">
<title>QWT Two Day Training Event</title>
<link rel="stylesheet" href="https://fonts.googleapis.com/css2?family=Arvo:ital,wght@1,700&family=Noto+Serif:wght@700&family=Open+Sans:wght@600;700&display=swap">
<style>
  :root {
    --cream: #fbf3d4;
    --gold-light: #f3dca0;
    --gold: #e2b060;
    --amber: #c98a3c;
    --navy: #0b0a3a;
    --navy-deep: #05042a;
    --ink: #1c2150;
    --royal: #1010d8;
    --accent-blue: #1a20d0;
  }
  * { margin: 0; padding: 0; box-sizing: border-box; }
  html, body {
    width: 1200px;
    height: 800px;
    overflow: hidden;
    background: var(--navy-deep);
  }
  .postcard {
    position: relative;
    width: 1200px;
    height: 800px;
    overflow: hidden;
  }
  .glow-backdrop {
    position: absolute;
    inset: 0;
    background:
      radial-gradient(ellipse 55% 45% at 50% 40%, var(--cream) 0%, rgba(251,243,212,0) 70%),
      radial-gradient(ellipse 45% 55% at 92% 70%, var(--amber) 0%, rgba(201,138,60,0) 70%),
      radial-gradient(ellipse 40% 50% at 6% 70%, var(--gold) 0%, rgba(226,176,96,0) 70%),
      linear-gradient(180deg, var(--gold-light) 0%, var(--gold) 70%, var(--amber) 100%);
  }
  .wave {
    position: absolute;
    left: 0;
    top: 0;
    width: 1200px;
    height: 800px;
  }
  .content {
    position: absolute;
    inset: 0;
    text-align: center;
    color: var(--ink);
  }
  .brand-mark {
    position: absolute;
    top: 30px;
    left: 0;
    right: 0;
    font-family: "Noto Serif", serif;
    font-weight: 700;
    font-size: 72px;
    line-height: 1;
    color: var(--royal);
  }
  .host-line {
    position: absolute;
    top: 122px;
    left: 0;
    right: 0;
    font-family: "Noto Serif", serif;
    font-weight: 700;
    font-size: 31px;
    line-height: 38px;
    letter-spacing: 0.5px;
  }
  .headline {
    position: absolute;
    left: 0;
    right: 0;
    font-family: "Arvo", serif;
    font-style: italic;
    font-weight: 700;
    font-size: 66px;
    line-height: 1;
    letter-spacing: 2px;
    color: var(--royal);
    text-shadow: 3px 3px 3px rgba(40, 30, 10, 0.55);
  }
  .headline-training { top: 220px; }
  .headline-party { top: 358px; letter-spacing: 3px; }
  .connector {
    position: absolute;
    top: 302px;
    left: 0;
    right: 0;
    font-family: "Open Sans", sans-serif;
    font-weight: 600;
    font-size: 40px;
    line-height: 1;
  }
  .detail {
    position: absolute;
    text-align: center;
  }
  .detail-date { left: 150px; width: 520px; top: 492px; }
  .detail-time { left: 640px; width: 320px; top: 492px; }
  .detail-label {
    font-family: "Open Sans", sans-serif;
    font-weight: 700;
    font-size: 34px;
    line-height: 44px;
    color: var(--accent-blue);
    letter-spacing: 1px;
  }
  .detail-time .detail-label { font-size: 31px; letter-spacing: 2px; }
  .detail-value {
    font-family: "Noto Serif", serif;
    font-weight: 700;
    font-size: 38px;
    line-height: 48px;
    letter-spacing: 1px;
  }
  .detail-value sup { font-size: 19px; vertical-align: 15px; }
  .venue {
    position: absolute;
    top: 608px;
    left: 0;
    right: 0;
    font-family: "Noto Serif", serif;
    font-weight: 700;
    font-size: 32px;
    line-height: 44px;
    letter-spacing: 1px;
  }
  .venue-label {
    font-family: "Open Sans", sans-serif;
    color: var(--accent-blue);
    margin-right: 18px;
    letter-spacing: 2px;
  }
</style>
</head>
<body>
  <main class="postcard">
    <div class="glow-backdrop" role="img" aria-label="Soft golden bokeh light background"></div>

    <svg class="wave" viewBox="0 0 1200 800" aria-hidden="true">
      <path d="M0,569 C200,615 400,690 700,725 C950,752 1100,680 1200,612 L1200,800 L0,800 Z" fill="var(--navy)"/>
      <path d="M0,612 C200,660 400,735 700,768 C950,795 1100,722 1200,658 L1200,672 C1100,738 950,810 700,784 C400,752 200,676 0,628 Z" fill="var(--cream)" opacity="0.95"/>
      <path d="M0,628 C200,676 400,752 700,784 C950,810 1100,738 1200,672 L1200,800 L0,800 Z" fill="var(--navy-deep)"/>
    </svg>

    <section class="content">
      <div class="brand-mark">QWT</div>
      <p class="host-line">QWT Quarry West Trust<br>is hosting</p>
      <h1 class="headline headline-training">Two Day Training Event</h1>
      <p class="connector">and</p>
      <h2 class="headline headline-party">a Dinner/Bowling Party</h2>

      <div class="detail detail-date">
        <p class="detail-label">On</p>
        <p class="detail-value">16<sup>th</sup> &amp; 17<sup>th</sup> Sept, 2019</p>
      </div>
      <div class="detail detail-time">
        <p class="detail-label">From</p>
        <p class="detail-value">14.00 - 20.30</p>
      </div>

      <p class="venue"><span class="venue-label">Venue:</span>Harrowgate Conference Hall in Troy, MI</p>
    </section>
  </main>
</body>
</html>
```